Bref créative
BrightPath Fuel
Eye Catching Card & Letterhead Design
Professional
Marcus Torres
CEO
4183 HAWTHORNE AVE
SUITE 310
SARASOTA FL 34519
mtorres@brightpathfuel.example
www.brightpathfuel.example
use the WELL portion of the logo and list the twitter site (@brightpathfuel)

```html
<!DOCTYPE html>
<html lang="en">
<head>
<meta charset="utf-8">
<title>BrightPath Fuel – Business Card</title>
<link href="https://fonts.googleapis.com/css2?family=Open+Sans:wght@400;600;700&family=Titillium+Web:wght@400;700&display=swap" rel="stylesheet">
<style>
  :root {
    --bg: #e9e6e1;
    --card: #ffffff;
    --green: #8cc63f;
    --green-soft: #dcedc4;
    --ink: #3a3a3a;
    --grey: #6b6b6b;
  }
  * { box-sizing: border-box; margin: 0; padding: 0; }
  html, body { width: 1200px; height: 739px; overflow: hidden; }
  body {
    background: var(--bg);
    font-family: "Open Sans", Arial, sans-serif;
    color: var(--ink);
    position: relative;
  }
  .card {
    position: absolute;
    top: 226px;
    width: 500px;
    height: 286px;
    background: var(--card);
    box-shadow: 0 4px 14px rgba(0,0,0,0.18);
    overflow: hidden;
  }
  .card--front { left: 70px; }
  .card--back { left: 630px; }

  /* Front */
  .front-mark {
    position: absolute;
    top: 92px; left: 0; right: 0;
    display: flex; justify-content: center; align-items: center; gap: 10px;
  }
  .mark-dot {
    width: 22px; height: 22px; border-radius: 50%;
    background: var(--green);
  }
  .wordmark {
    font-family: "Titillium Web", Arial, sans-serif;
    font-weight: 700;
    color: var(--green);
    letter-spacing: 1px;
    text-transform: uppercase;
  }
  .front-mark .wordmark { font-size: 30px; }
  .front-url {
    position: absolute;
    top: 160px; left: 0; right: 0;
    text-align: center;
    font-size: 13px; font-weight: 700; color: var(--ink);
  }

  /* Back */
  .back-watermark {
    position: absolute;
    top: 40px; right: 26px;
    font-family: "Titillium Web", Arial, sans-serif;
    font-weight: 700;
    font-size: 44px;
    color: var(--green-soft);
    text-transform: uppercase;
    line-height: 1;
  }
  .back-mark {
    position: absolute;
    top: 112px; left: 30px;
    display: flex; align-items: center; gap: 8px;
  }
  .back-mark .mark-dot { width: 18px; height: 18px; }
  .back-mark .wordmark { font-size: 27px; }
  .person {
    position: absolute; top: 160px; left: 30px;
    font-size: 11px; font-weight: 700; color: var(--green);
  }
  .person .title { color: var(--grey); font-weight: 600; }
  .address {
    position: absolute; top: 182px; left: 30px;
    font-size: 9.5px; line-height: 1.45; color: var(--grey);
    text-transform: uppercase;
  }
  .contacts {
    position: absolute; top: 216px; left: 30px;
    list-style: none;
    font-size: 9.5px; color: var(--grey);
  }
  .contacts li { display: flex; align-items: center; gap: 6px; height: 14px; }
  .contacts svg { width: 10px; height: 10px; flex: none; }
</style>
</head>
<body>
  <section class="card card--front" aria-label="Card front">
    <div class="front-mark">
      <span class="mark-dot"></span>
      <span class="wordmark">BrightPath Fuel</span>
    </div>
    <p class="front-url">www.brightpathfuel.example</p>
  </section>

  <section class="card card--back" aria-label="Card back">
    <div class="back-watermark" aria-hidden="true">BrightPath</div>
    <div class="back-mark">
      <span class="mark-dot"></span>
      <span class="wordmark">BrightPath Fuel</span>
    </div>
    <p class="person">Marcus Torres <span class="title">/ CEO</span></p>
    <p class="address">4183 Hawthorne Ave Suite 310<br>Sarasota FL 34519</p>
    <ul class="contacts">
      <li>
        <svg viewBox="0 0 10 10"><circle cx="5" cy="5" r="5" fill="#8cc63f"/><path d="M3.3 2.6l1 1-.6.7a3.6 3.6 0 0 0 2 2l.7-.6 1 1-.8.8C4.8 7.3 2.7 5.2 2.5 3.4z" fill="#fff"/></svg>
        555.014.2290
      </li>
      <li>
        <svg viewBox="0 0 10 10"><circle cx="5" cy="5" r="5" fill="#8cc63f"/><rect x="2.4" y="3.2" width="5.2" height="3.6" fill="none" stroke="#fff" stroke-width=".8"/><path d="M2.4 3.2L5 5.2l2.6-2" fill="none" stroke="#fff" stroke-width=".8"/></svg>
        mtorres@brightpathfuel.example
      </li>
      <li>
        <svg viewBox="0 0 10 10"><circle cx="5" cy="5" r="5" fill="#8cc63f"/><circle cx="5" cy="5" r="1.6" fill="none" stroke="#fff" stroke-width=".8"/><path d="M6.6 4.2v1.6c0 .9 1 .9 1 0V5A2.6 2.6 0 1 0 6.4 7.2" fill="none" stroke="#fff" stroke-width=".8"/></svg>
        @brightpathfuel
      </li>
      <li>
        <svg viewBox="0 0 10 10"><circle cx="5" cy="5" r="5" fill="#8cc63f"/><circle cx="5" cy="5" r="2.6" fill="none" stroke="#fff" stroke-width=".7"/><path d="M2.4 5h5.2M5 2.4c-1.4 1.6-1.4 3.6 0 5.2M5 2.4c1.4 1.6 1.4 3.6 0 5.2" fill="none" stroke="#fff" stroke-width=".6"/></svg>
        www.brightpathfuel.example
      </li>
    </ul>
  </section>
</body>
</html>
```